Website Design for BrelvoHub.com

BrelvoHub.com offers military researchers, reunion coordinators, military museums and others access to over 13 million military personnel records including the Internet's only Corvane Service Archive Index, Tessel Squad Ledger and Orlith Service Ledger.

We are currently going through a rebranding and website redesign. We require a modern, "web 2.0" design consistent with the quality expected of most technology start-ups. Please use the logo below for your design:

http://tpalm.vendrix.com/brhb_content/brelvoHub_LOGO.jpg [JPG]
http://tpalm.vendrix.com/brhb_content/brelvoHub_LOGO.psd [PSD]

```html
<!DOCTYPE html>
<html lang="en">
<head>
<meta charset="utf-8">
<title>BrelvoHub – Databases</title>
<link rel="stylesheet" href="https://fonts.googleapis.com/css2?family=Arimo:wght@400;700&family=Open+Sans:wght@400;700;800&display=swap">
<style>
  :root {
    --page-white: #ffffff;
    --band-light: #cfdcb6;
    --band-mid: #7d9a52;
    --band-dark: #1d3510;
    --panel-light: #eef2e6;
    --panel-mid: #d6e0c4;
    --ribbon: #3f6a12;
    --ribbon-text: #d9f2a6;
    --heading: #1b2a10;
    --body-text: #5a5a5a;
    --button: #456f16;
    --footer-camo: #24401a;
    --footer-bar: #3d6b0f;
    --footer-text: #ffffff;
    --logo-grey: #555a5e;
  }
  * { box-sizing: border-box; margin: 0; padding: 0; }
  html, body { width: 1051px; height: 1200px; overflow: hidden; }
  body {
    position: relative;
    font-family: "Arimo", Arial, sans-serif;
    background:
      linear-gradient(to bottom,
        var(--page-white) 0px, var(--page-white) 205px,
        var(--band-light) 230px, var(--band-mid) 322px,
        var(--band-dark) 329px, var(--band-dark) 640px,
        #6f8462 820px, #d8ddd2 960px, var(--page-white) 1060px);
  }
  .site-logo {
    position: absolute; display: flex; align-items: center; gap: 12px;
  }
  .site-logo__mark { width: 34px; height: 34px; }
  .site-logo__name { font-weight: 400; letter-spacing: 1px; }
  .site-logo--header { left: 72px; top: 36px; }
  .site-logo--header .site-logo__mark { background: var(--logo-grey); }
  .site-logo--header .site-logo__name { font-size: 28px; color: var(--logo-grey); }

  .content-panel {
    position: absolute; left: 63px; top: 117px; width: 924px; height: 868px;
    background: linear-gradient(100deg, var(--panel-mid) 0%, var(--panel-light) 40%, #f2f3ee 65%, var(--panel-mid) 100%);
    border: 1px solid #ffffff;
    box-shadow: 0 0 14px rgba(0,0,0,0.35);
  }
  .section-ribbon { position: absolute; left: 0; top: 75px; width: 442px; height: 86px; }
  .section-ribbon h1 {
    position: absolute; left: 60px; top: 12px;
    font-family: "Open Sans", Verdana, sans-serif; font-weight: 800;
    font-size: 50px; letter-spacing: 1px; color: var(--ribbon-text);
  }
  .record-list { position: absolute; left: 108px; top: 200px; width: 770px; list-style: none; }
  .record { position: relative; height: 162px; }
  .record__title {
    font-size: 12.5px; color: var(--heading); text-decoration: underline;
    font-weight: 400; height: 19px;
  }
  .record__title strong { font-weight: 700; }
  .record__photo {
    position: absolute; left: 0; top: 17px; width: 241px; height: 111px;
    border: 4px solid #ffffff; outline: 1px solid #b9beb2;
    box-shadow: 0 1px 3px rgba(0,0,0,0.2);
  }
  .record__text {
    position: absolute; left: 255px; top: 23px; width: 470px;
    font-family: "Open Sans", Verdana, sans-serif; font-size: 12.6px; line-height: 13.2px;
    color: var(--body-text); text-align: justify; letter-spacing: 0.15px;
  }
  .record__more {
    position: absolute; left: 660px; top: 107px; width: 58px; height: 16px;
    background: var(--button); color: #ffffff;
    font-family: "Open Sans", Verdana, sans-serif; font-size: 6px; font-weight: 700;
    line-height: 16px; padding-left: 6px; text-decoration: none;
    clip-path: polygon(0 0, 88% 0, 100% 50%, 88% 100%, 0 100%);
    box-shadow: 0 1px 2px rgba(0,0,0,0.3);
  }
  .photo--ww2 { background: linear-gradient(160deg, #9a9a9a, #3c3c3c 60%, #6b6b6b); }
  .photo--vietnam { background: linear-gradient(120deg, #1e1e28, #3a3a48 50%, #b9b4a4); }
  .photo--contemporary { background: linear-gradient(110deg, #27335a 0%, #3f4e7e 35%, #c9a646 60%, #7c2a24 85%); }
  .photo--gulf { background: radial-gradient(circle at 45% 45%, #e8d3b2 0%, #c9a983 55%, #5a4630 100%); }

  .site-footer {
    position: absolute; left: 63px; top: 1002px; width: 924px; height: 125px;
    background: linear-gradient(90deg, var(--footer-camo), #2f4f22 50%, var(--footer-camo));
  }
  .site-logo--footer { left: 40px; top: 44px; }
  .site-logo--footer .site-logo__mark { background: #ffffff; width: 36px; height: 36px; }
  .site-logo--footer .site-logo__name { font-size: 30px; color: #ffffff; }
  .footer-divider { position: absolute; left: 392px; top: 28px; width: 1px; height: 72px; background: rgba(255,255,255,0.15); }
  .footer-nav { position: absolute; top: 28px; list-style: none; font-size: 12.5px; line-height: 17px; color: var(--footer-text); }
  .footer-nav--primary { left: 417px; }
  .footer-nav--secondary { left: 535px; }
  .footer-social { position: absolute; left: 654px; top: 44px; display: flex; align-items: center; gap: 12px; font-size: 10px; color: var(--footer-text); }
  .footer-social__item { display: flex; align-items: center; gap: 6px; }
  .footer-social__icon { width: 12px; height: 12px; }
  .icon--pipwave { background: #5fb4e6; }
  .icon--friendora { background: #3b5b99; }
  .icon--rss { background: #f08a24; }
  .footer-bar {
    position: absolute; left: 63px; top: 1127px; width: 924px; height: 33px;
    background: var(--footer-bar); color: var(--footer-text);
    font-size: 12px; text-align: center; line-height: 33px;
  }
</style>
</head>
<body>
  <header class="site-logo site-logo--header">
    <span class="site-logo__mark"></span>
    <span class="site-logo__name">BrelvoHub</span>
  </header>

  <main class="content-panel">
    <div class="section-ribbon">
      <svg width="442" height="86" viewBox="0 0 442 86" aria-hidden="true">
        <polygon points="0,0 414,0 442,43 414,86 0,86" fill="#3f6a12"/>
        <polygon points="0,0 414,0 420,9 0,9" fill="#4f7d1c"/>
      </svg>
      <h1>DATABASES</h1>
    </div>

    <ul class="record-list">
      <li class="record">
        <h2 class="record__title"><strong>World War II</strong> "1940 - 1946"</h2>
        <div class="record__photo photo--ww2" role="img" aria-label="Black and white photo of a soldiers memorial statue"></div>
        <p class="record__text">Lorem Ipsum is simply dummy text of the printing and typesetting dustry. Lorem Ipsum has been the industry's standard dummy text ever since the 1500s, when an unknown printer took a galley of type and scrambled it to make a type specimen book. It has survived not only five centuries, but also the leap into electronic typesetting, remaining essent.</p>
        <a class="record__more" href="#">READ MORE</a>
      </li>
      <li class="record">
        <h2 class="record__title"><strong>Vietnam</strong> "1955-1975"</h2>
        <div class="record__photo photo--vietnam" role="img" aria-label="Photo of Vietnam era military patches and pins"></div>
        <p class="record__text">Lorem Ipsum is simply dummy text of the printing and typesetting dustry. Lorem Ipsum has been the industry's standard dummy text ever since the 1500s, when an unknown printer took a galley of type and scrambled it to make a type specimen book. It has survived not only five centuries, but also the leap into electronic typesetting, remaining essent.</p>
        <a class="record__more" href="#">READ MORE</a>
      </li>
      <li class="record">
        <h2 class="record__title"><strong>Contemporary Military Records</strong> "1990s - 2001"</h2>
        <div class="record__photo photo--contemporary" role="img" aria-label="Photo of service medals on a flag"></div>
        <p class="record__text">Lorem Ipsum is simply dummy text of the printing and typesetting dustry. Lorem Ipsum has been the industry's standard dummy text ever since the 1500s, when an unknown printer took a galley of type and scrambled it to make a type specimen book. It has survived not only five centuries, but also the leap into electronic typesetting, remaining essent.</p>
        <a class="record__more" href="#">READ MORE</a>
      </li>
      <li class="record">
        <h2 class="record__title"><strong>Gulf War</strong> "1991"</h2>
        <div class="record__photo photo--gulf" role="img" aria-label="Sepia photo of a magnifying glass over a map of Iraq"></div>
        <p class="record__text">Lorem Ipsum is simply dummy text of the printing and typesetting dustry. Lorem Ipsum has been the industry's standard dummy text ever since the 1500s, when an unknown printer took a galley of type and scrambled it to make a type specimen book. It has survived not only five centuries, but also the leap into electronic typesetting, remaining essent.</p>
        <a class="record__more" href="#">READ MORE</a>
      </li>
    </ul>
  </main>

  <footer class="site-footer">
    <div class="site-logo site-logo--footer">
      <span class="site-logo__mark"></span>
      <span class="site-logo__name">BrelvoHub</span>
    </div>
    <div class="footer-divider"></div>
    <ul class="footer-nav footer-nav--primary">
      <li>- Home</li>
      <li>- Databases</li>
      <li>- Resources</li>
      <li>- About</li>
    </ul>
    <ul class="footer-nav footer-nav--secondary">
      <li>- Contact</li>
      <li>- Privacy</li>
      <li>- Advertise</li>
    </ul>
    <div class="footer-social">
      <span>Follow us:</span>
      <span class="footer-social__item"><span class="footer-social__icon icon--pipwave"></span>Pipwave</span>
      <span class="footer-social__item"><span class="footer-social__icon icon--friendora"></span>Friendora</span>
      <span class="footer-social__item"><span class="footer-social__icon icon--rss"></span>RSS</span>
    </div>
  </footer>
  <div class="footer-bar">All Rights Reserved © 2013 - brelvohub.com</div>
</body>
</html>
```